Flyer FMLP

Everyone deserves true happiness.
Real Food is the answer to:
A body you love
Reverting illnesses
Healthy digestion
Stable blood sugar
Emotions in control
Blasting energy
Sound sleep
REAL food + water + exercise + Laughter =
“HIGH QUALITY OF LIFE “
EASY, right?
Challenging: certainly
Changing habits: reluctance in sight!
WE’RE OFFER TO:
1. Study YOUR unique body composition, food cravings, blockages, illnesses, and personality!
2. Introduce you to new Food
3. customized wellness plan with follow ups
4. meditation,cooking, and fitness classes as well as wellness workshops
5. New friends with high aspirations
LOGO
Contact info
Please visit our web address to see our design style and colors: www.freshmeadowlifepath.net
Target Market(s)
people who want to be more healthy
Industry/Entity Type
Fitness
Requirements
Must have
- beautiful pictures of fresh food (main picture) and maybe a few more small pictures reflecting
exercise
healthy living
meditation
Nice to have
- look is crucial. recall some of the color or colors from my logo to have a theme

```html
<!DOCTYPE html>
<html lang="en">
<head>
<meta charset="UTF-8">
<title>FMLP Flyer Set</title>
<link href="https://fonts.googleapis.com/css2?family=PT+Sans:ital,wght@0,400;0,700;1,400;1,700&family=PT+Serif&display=swap" rel="stylesheet">
<style>
  :root{
    --page:#ece7e2;
    --white:#ffffff;
    --green:#2f9a3b;
    --green-dark:#1e7a2b;
    --yellow:#f6c415;
    --orange:#e98b1a;
    --red:#d2232a;
    --navy:#2a2f8c;
    --ink:#2a2a2a;
    --sans:"PT Sans", Arial, sans-serif;
    --serif:"PT Serif", Georgia, serif;
  }
  *{box-sizing:border-box;margin:0;padding:0}
  html,body{width:1200px;height:800px;overflow:hidden;background:var(--page);font-family:var(--sans)}
  .canvas{position:relative;width:1200px;height:800px}
  .piece{position:absolute;overflow:hidden;box-shadow:0 6px 18px rgba(0,0,0,.25)}
  .piece > svg{position:absolute;inset:0}
  .abs{position:absolute}
  .photo{position:absolute}

  /* brand mark */
  .brand{position:absolute;display:flex;align-items:center;gap:5px}
  .brand-dot{width:20px;height:20px;border-radius:50%;background:var(--green)}
  .brand-name{font-family:var(--sans);font-weight:700;color:var(--green-dark);font-size:15px;line-height:1}
  .brand-tag{position:absolute;font-size:5.5px;font-weight:700;color:var(--ink);letter-spacing:.2px}

  /* front flyer */
  .front{left:40px;top:175px;width:400px;height:450px}
  .headline{font-weight:700;color:var(--green);font-size:30px;line-height:1;text-align:right}
  .subline{font-size:15px;color:var(--red);text-align:right;line-height:1.1}
  .subline b{font-weight:700}
  .testimonial{left:8px;top:200px;width:150px;color:var(--white)}
  .testimonial h3{font-size:9px;color:var(--red);font-weight:700;margin-bottom:3px}
  .testimonial p{font-size:6.3px;line-height:1.35}
  .testimonial .who{font-weight:700;margin-top:8px;font-size:7px}
  .address{left:10px;top:396px;width:88px;font-size:6px;line-height:1.5;color:var(--white)}
  .call{left:108px;top:395px;color:var(--red);font-weight:700;font-size:9px;line-height:1}
  .call .phone{display:block;color:var(--white);font-size:14px;margin-top:2px}
  .url{left:10px;bottom:7px;color:var(--red);font-weight:700;font-size:9.5px}
  .slogan{right:14px;bottom:14px;text-align:right;font-weight:700;line-height:1.05}
  .slogan .line-a{display:block;color:var(--ink);font-size:14px}
  .slogan .line-b{display:block;color:var(--white);font-size:17px}

  /* back flyer */
  .back{left:470px;top:175px;width:370px;height:450px}
  .col-left{left:0;top:0;width:185px;height:450px}
  .col-right{left:185px;top:0;width:185px;height:450px}
  .happy{left:12px;top:16px;font-style:italic;font-size:17px;line-height:1.15}
  .happy .a{display:block;color:var(--red)}
  .happy .b{display:block;color:var(--navy);font-weight:700;padding-left:38px}
  .list-head{font-weight:700;color:var(--navy);font-size:9.5px}
  .real-list{left:10px;top:178px}
  .real-list ul{list-style:none;margin-top:3px}
  .real-list li{font-family:var(--serif);color:var(--white);font-size:11px;line-height:14.5px}
  .formula{left:195px;top:8px;width:170px;font-style:italic;font-size:9px;line-height:1.2}
  .formula .red{color:var(--red)}
  .formula .big{display:block;color:var(--navy);font-weight:700;font-size:14px;margin:1px 0 2px}
  .formula .strong{font-weight:700}
  .offer{left:195px;top:228px;width:168px}
  .offer ol{list-style:none;margin-top:3px}
  .offer li{color:var(--white);font-size:7.8px;line-height:1.35}
  .offer li b{font-weight:700}

  /* rack card */
  .rack{left:880px;top:100px;width:250px;height:600px}
  .rack .headline{font-size:32px}
  .rack .subline{font-size:16px}
  .rack .slogan .line-a{font-size:18px}
  .rack .slogan .line-b{font-size:20px}
</style>
</head>
<body>
<div class="canvas">

  <!-- Front flyer -->
  <section class="piece front">
    <svg width="400" height="450" viewBox="0 0 400 450">
      <defs>
        <linearGradient id="warmFront" x1="0" y1="0" x2="0" y2="1">
          <stop offset="0" stop-color="#f7c917"/>
          <stop offset=".55" stop-color="#eea01b"/>
          <stop offset="1" stop-color="#e07414"/>
        </linearGradient>
        <linearGradient id="greenBand" x1="0" y1="0" x2="1" y2="1">
          <stop offset="0" stop-color="#5bb847"/>
          <stop offset="1" stop-color="#1e7a2b"/>
        </linearGradient>
      </defs>
      <rect width="400" height="450" fill="url(#warmFront)"/>
      <path d="M178,0 H400 V130 C335,140 255,160 225,225 C205,160 188,95 178,0Z" fill="#ffffff"/>
      <path d="M0,150 C60,158 140,150 185,0 L200,0 C175,150 90,175 0,170Z" fill="url(#greenBand)"/>
      <path d="M30,175 C80,280 160,410 265,402 C350,395 396,300 400,130 L400,118 C385,290 340,378 265,380 C175,385 100,275 30,175Z" fill="url(#greenBand)"/>
      <circle cx="290" cy="275" r="108" fill="#ffffff"/>
    </svg>
    <div class="photo" role="img" aria-label="Group practising yoga in a sunny park"
         style="left:0;top:0;width:185px;height:150px;background:linear-gradient(160deg,#b9d98a,#6f9f46 60%,#4d7a33);border-bottom-right-radius:60px 40px"></div>
    <div class="photo" role="img" aria-label="Smiling woman giving thumbs up behind a bowl of fresh fruit and vegetables"
         style="left:188px;top:173px;width:204px;height:204px;border-radius:50%;background:linear-gradient(180deg,#e6d6c8,#c9c29a 55%,#8fb04a)"></div>

    <div class="brand" style="left:222px;top:24px">
      <span class="brand-dot"></span><span class="brand-name">Freshmeadowlifepath</span>
    </div>
    <div class="brand-tag" style="left:248px;top:46px">BALANCED NUTRITION, MIND, AND FITNESS</div>

    <div class="abs" style="right:18px;top:105px">
      <div class="headline">ENJOY</div>
      <div class="subline">life to the <b>FULLEST</b></div>
    </div>

    <div class="abs testimonial">
      <h3>Testimonials</h3>
      <p>I came to Marina during a very crucial life change. I found her to be patient, kind, enthusiastic, honest, helpful &amp; most importantly a wonderful listener. Marina was able to create a nutrition guide suitable even for my picky eating habits. I have learned to introduce new fruits and vegetables into my palate &amp; wouldn't have thought of doing so without Marina's suggestions of different cooking methods. Marina inspires me to be healthier &amp; for that I am forever grateful.</p>
      <p class="who">Dana R. –pre-sales, Lakeview, FL</p>
    </div>

    <div class="abs address">Your Address will be come here<br>Your Address will be come here<br>Email: mail@fmlp.net</div>
    <div class="abs call">PLEASE CALL NOW<span class="phone">407-555-0148</span></div>
    <div class="abs url">www.freshmeadowlifepath.net</div>
    <div class="abs slogan"><span class="line-a">SEE FOOD AS YOUR</span><span class="line-b">FRIEND AND YOUR HEALER</span></div>
  </section>

  <!-- Back flyer -->
  <section class="piece back">
    <div class="abs col-left" style="background:linear-gradient(180deg,#f8cd1c,#f0a81b 60%,#e88a17)"></div>
    <div class="abs col-right" style="background:linear-gradient(180deg,#f4b41a,#ec9418 50%,#e27d15);border-left:1px solid #fff3"></div>

    <div class="abs happy"><span class="a">Everyone deserves</span><span class="b">TRUE HAPPINESS</span></div>
    <div class="photo" role="img" aria-label="Red apple wrapped in a yellow measuring tape"
         style="left:30px;top:64px;width:125px;height:100px;background:linear-gradient(180deg,#e8a22a,#d9732a)"></div>
    <div class="abs real-list">
      <div class="list-head">REAL FOOD IS THE ANSWER TO:</div>
      <ul>
        <li>A body you love</li>
        <li>Reverting illnesses</li>
        <li>Healthy digestion</li>
        <li>Stable blood sugar</li>
        <li>Emotions in control</li>
        <li>Blasting energy</li>
        <li>Sound sleep</li>
      </ul>
    </div>
    <div class="photo" role="img" aria-label="Man sleeping peacefully on a white pillow"
         style="left:0;top:312px;width:185px;height:138px;background:linear-gradient(135deg,#c9d3e6,#eef1f6 45%,#8a9fc2)"></div>

    <div class="abs formula">
      <span class="red">REAL food + water + exercise + Laughter =</span>
      <span class="big">“HIGH QUALITY OF LIFE “</span>
      <span class="red strong">EASY, right?</span><br>
      <span class="red">Challenging: certainly</span><br>
      <span class="red strong">Changing habits: reluctance in sight!</span>
    </div>
    <div class="photo" role="img" aria-label="Fitness class stretching in a bright gym"
         style="left:185px;top:97px;width:185px;height:120px;background:linear-gradient(180deg,#dfe6ee,#9fb6cf 55%,#5a7aa3)"></div>
    <div class="abs offer">
      <div class="list-head">WE’RE OFFER TO:</div>
      <ol>
        <li><b>1. Study</b> YOUR unique body composition, food cravings, blockages, illnesses, and personality!</li>
        <li><b>2. Introduce</b> you to new Food</li>
        <li><b>3. Customized</b> wellness plan with follow ups</li>
        <li><b>4. Meditation,</b> cooking, and fitness classes as well as wellness workshops</li>
        <li><b>5. New friends</b> with high aspirations</li>
      </ol>
    </div>
    <div class="photo" role="img" aria-label="Two women talking during a wellness consultation"
         style="left:185px;top:393px;width:92px;height:57px;background:linear-gradient(135deg,#e9dcc6,#b89a78)"></div>
    <div class="photo" role="img" aria-label="Step aerobics class in a studio"
         style="left:279px;top:393px;width:91px;height:57px;background:linear-gradient(135deg,#f0e6da,#c9a887)"></div>
  </section>

  <!-- Rack card -->
  <section class="piece rack">
    <svg width="250" height="600" viewBox="0 0 250 600">
      <defs>
        <linearGradient id="warmRack" x1="0" y1="0" x2="0" y2="1">
          <stop offset="0" stop-color="#f4ae1a"/>
          <stop offset="1" stop-color="#e07414"/>
        </linearGradient>
        <linearGradient id="greenRack" x1="0" y1="0" x2="1" y2="1">
          <stop offset="0" stop-color="#5bb847"/>
          <stop offset="1" stop-color="#1e7a2b"/>
        </linearGradient>
      </defs>
      <rect width="250" height="600" fill="#ffffff"/>
      <path d="M0,250 C40,360 100,460 170,462 C220,464 245,420 250,380 V600 H0Z" fill="url(#warmRack)"/>
      <path d="M0,230 C40,350 100,445 170,446 C218,447 245,410 250,360 V385 C240,440 215,470 170,470 C95,470 35,375 0,265Z" fill="url(#greenRack)"/>
      <circle cx="140" cy="330" r="108" fill="#ffffff"/>
    </svg>
    <div class="photo" role="img" aria-label="Smiling woman giving thumbs up behind a bowl of fresh fruit and vegetables"
         style="left:38px;top:228px;width:204px;height:204px;border-radius:50%;background:linear-gradient(180deg,#e6d6c8,#c9c29a 55%,#8fb04a)"></div>

    <div class="brand" style="left:22px;top:26px">
      <span class="brand-dot"></span><span class="brand-name">Freshmeadowlifepath</span>
    </div>
    <div class="brand-tag" style="left:48px;top:48px">BALANCED NUTRITION, MIND, AND FITNESS</div>

    <div class="abs" style="right:22px;top:105px">
      <div class="headline">ENJOY</div>
      <div class="subline">life to the <b>FULLEST</b></div>
    </div>

    <div class="abs slogan" style="right:14px;bottom:30px"><span class="line-a">SEE FOOD AS YOUR</span><span class="line-b">FRIEND AND YOUR HEALER</span></div>
  </section>

</div>
</body>
</html>
```